Digital Invitation to Grand Opening of Newest Cabaret Show

Grand Opening of The Velvet Herons newest venue MIRVOLANT
We are a show venue where we put on multiple shows through out the year https://www.velvetheronvenues.example/brisbane/
Please find shows on the website and trailers so understand the vibe. We are wanting a world class, exciting, show focus invitation.
All invitations are the same just with different text.
Please have the focus being a new venue focus rather than being a SHOW focus.
so
WING IT! VELVET HERON HAS ARRIVED IN BRISBANE!
GRAND OPENING OF THE VELVET HERON MIRVOLANT.
The newest entertainment destination
INVITATION ONE
Date: Thursday 7th December - Media and Publicity Performance of Lumèra
Location: 41 Tarrowin Street, Hamilton, QLD 4007
Gates Open: 5.30pm
Show Start: 7.30pm
RSVP: dora@doramilby.example
Dress Code: Lumeradazzle
INVITATION TWO:
Date:Thursday 7th December - Media and Publicity Performance of Lumèra
Gates Open: 5.30pm
Show Start: 7.30pm
RSVP: hello@quillmarsh.example.au
Dress Code: Lumeradazzle
INVITATION THREE:
Date: Friday 8th December - ZUMO listener party for Lumèra
Gates Open: 5.30pm
Show Start: 7.30pm
INVITATION FOUR:
Date: Saturday 9th December - Velvet Heron Gala VIP Opening Lumèra
Gates Open: 5.30pm
Show Start: 7.30pm
RSVP: maren@vhvx.example.au
Dress Code: Lumeradazzle (Black Tie)
Make it pink, show focused, entertaining, cabaret, theatre, world class, glamour, glitz
Target Market(s)
25 - 55
Look and feel

```html
<!DOCTYPE html>
<html lang="en">
<head>
<meta charset="utf-8">
<title>Velvet Heron Mirvolant – Grand Opening Invitations</title>
<link rel="stylesheet" href="https://fonts.googleapis.com/css2?family=Montserrat:wght@300;400;500;600;700;900&family=Sacramento&display=swap">
<style>
  :root {
    --board-light: #cc86bb;
    --board-deep: #c33c9f;
    --card-black: #050208;
    --haze-purple: #5a1c8c;
    --neon-pink: #f26ad8;
    --neon-pink-soft: #ffb3f0;
    --neon-glow: rgba(255, 60, 210, 0.85);
    --ice-blue: #d9ecff;
    --ice-glow: rgba(90, 150, 255, 0.9);
    --marquee-gold: #f4c94e;
    --marquee-glow: rgba(255, 200, 70, 0.85);
    --white: #ffffff;
    --rule: rgba(255, 255, 255, 0.55);
  }
  * { box-sizing: border-box; margin: 0; padding: 0; }
  html, body { width: 951px; height: 1200px; overflow: hidden; }
  body {
    position: relative;
    background:
      radial-gradient(ellipse 70% 55% at 5% 95%, var(--board-deep) 0%, transparent 70%),
      linear-gradient(135deg, var(--board-light) 0%, #c97cb8 45%, var(--board-deep) 100%);
    font-family: "Montserrat", Arial, sans-serif;
  }

  .invite {
    position: absolute;
    width: 810px;
    height: 566px;
    overflow: hidden;
    background: var(--card-black);
    box-shadow: 0 10px 28px rgba(40, 0, 40, 0.45);
    transform-origin: top left;
  }
  .invite--main { left: 67px; top: 68px; }
  .invite--media { left: 67px; top: 870px; transform: scale(0.43); }
  .invite--listener { left: 303px; top: 778px; transform: scale(0.431); }
  .invite--gala { left: 526px; top: 677px; transform: scale(0.433); }

  .invite__haze {
    position: absolute; inset: 0;
    background:
      radial-gradient(ellipse 28% 30% at 30% 22%, rgba(120, 40, 160, 0.75), transparent 70%),
      radial-gradient(ellipse 40% 40% at 40% 45%, var(--haze-purple), transparent 75%),
      radial-gradient(ellipse 30% 16% at 55% 58%, rgba(200, 40, 180, 0.55), transparent 80%),
      radial-gradient(ellipse 40% 30% at 25% 70%, rgba(40, 30, 120, 0.6), transparent 80%);
  }
  .invite__streak {
    position: absolute; left: 0; top: 330px; width: 560px; height: 6px;
    background: linear-gradient(90deg, rgba(255, 60, 220, 0.1), rgba(255, 120, 240, 0.95) 40%, rgba(255, 60, 220, 0));
    box-shadow: 0 0 18px 6px rgba(230, 40, 200, 0.6);
  }

  .invite__photo {
    position: absolute; left: 100px; top: 132px; width: 390px; height: 356px;
    border-radius: 48% 48% 30% 30% / 40% 40% 20% 20%;
    background:
      radial-gradient(ellipse 50% 40% at 50% 70%, #e9b3e6, transparent 75%),
      radial-gradient(ellipse 60% 50% at 50% 35%, #b14fc0, transparent 80%),
      radial-gradient(ellipse 70% 60% at 50% 50%, #7a2c8f, transparent 85%);
    filter: blur(2px);
  }

  .invite__marquee {
    position: absolute; left: 18px; top: 22px; height: 512px;
    writing-mode: vertical-rl; transform: rotate(180deg);
    text-align: center;
    font-weight: 900; font-size: 92px; line-height: 92px; letter-spacing: 4px;
    color: var(--marquee-gold);
    background:
      radial-gradient(circle, #fff7d6 0 3px, transparent 4px) 0 0 / 16px 16px,
      linear-gradient(var(--marquee-gold), #d99b28);
    -webkit-background-clip: text; background-clip: text;
    -webkit-text-fill-color: transparent;
    filter: drop-shadow(0 0 6px var(--marquee-glow)) drop-shadow(0 0 14px rgba(255, 170, 40, 0.5));
  }

  .invite__copy {
    position: absolute; left: 388px; top: 0; width: 392px; height: 100%;
    text-align: center; color: var(--white);
  }
  .invite__copy > * { position: absolute; left: 0; right: 0; white-space: nowrap; }

  .kicker {
    top: 31px; font-size: 13px; font-weight: 500; letter-spacing: 1.6px; line-height: 16px;
    color: var(--neon-pink-soft);
    text-shadow: 0 0 6px var(--neon-glow), 0 0 12px var(--neon-glow);
  }
  .headline {
    font-weight: 900; line-height: 1; letter-spacing: -2px; color: var(--white);
    text-shadow: 2px 3px 0 #9a9a9a, 3px 5px 6px rgba(0, 0, 0, 0.6);
  }
  .headline--grand { top: 48px; font-size: 100px; letter-spacing: -3px; }
  .headline--opening { top: 138px; font-size: 76px; text-align: right; padding-right: 6px; }

  .of-the {
    top: 213px; display: flex; align-items: center; gap: 14px;
    font-size: 16px; font-weight: 500; line-height: 20px;
  }
  .of-the::before, .of-the::after { content: ""; flex: 1; height: 1px; background: var(--rule); }

  .venue-name {
    font-family: "Sacramento", cursive; font-size: 60px; line-height: 1;
    color: var(--neon-pink-soft);
    text-shadow: 0 0 4px var(--neon-pink), 0 0 12px var(--neon-glow), 0 0 24px var(--neon-glow);
  }
  .venue-name--first { top: 236px; }
  .venue-name--second { top: 286px; padding-left: 30px; }

  .divider { top: 356px; height: 1px; background: var(--rule); margin: 0 10px; }

  .event-date {
    top: 393px; font-size: 25px; line-height: 30px; font-weight: 400; letter-spacing: 0.3px;
    color: var(--ice-blue);
    text-shadow: 0 0 8px var(--ice-glow), 0 0 16px rgba(90, 150, 255, 0.6);
  }
  .event-date sup { font-size: 13px; vertical-align: 11px; line-height: 0; }
  .event-title { top: 433px; font-size: 13.5px; line-height: 18px; font-weight: 600; letter-spacing: 0; }
  .event-detail { font-size: 12.5px; line-height: 16px; font-weight: 400; letter-spacing: 0.1px; }
  .event-detail--times { top: 460px; }
  .event-detail--address { top: 478px; }
  .event-detail--rsvp { top: 497px; }
  .event-detail--dress { top: 516px; }
  .dress-script {
    font-family: "Sacramento", cursive; font-size: 28px; vertical-align: -5px;
    color: var(--neon-pink-soft);
    text-shadow: 0 0 6px var(--neon-glow);
  }
  .dress-note { top: 540px; font-size: 10px; line-height: 12px; padding-left: 120px; }

  .invite--listener .event-detail--dress { top: 497px; }
</style>
</head>
<body>

  <article class="invite invite--main">
    <div class="invite__haze"></div>
    <div class="invite__photo" role="img" aria-label="Photo of five cabaret dancers in pink feathered costumes with large pink feather fans"></div>
    <div class="invite__streak"></div>
    <div class="invite__marquee">WING IT!</div>
    <div class="invite__copy">
      <p class="kicker">VELVET HERON HAS ARRIVED IN BRISBANE</p>
      <h1 class="headline headline--grand">GRAND</h1>
      <h1 class="headline headline--opening">OPENING</h1>
      <p class="of-the">OF THE</p>
      <p class="venue-name venue-name--first">Velvet Heron</p>
      <p class="venue-name venue-name--second">Mirvolant</p>
      <div class="divider"></div>
      <p class="event-date">THURSDAY 7<sup>TH</sup> DECEMBER</p>
      <p class="event-title">MEDIA AND PUBLICITY PERFORMANCE OF LUMÈRA</p>
      <p class="event-detail event-detail--times">GATES OPEN 5:30 &nbsp;|&nbsp; SHOW START 7:30</p>
      <p class="event-detail event-detail--address">41 TARROWIN STREET, HAMILTON, QLD 4007</p>
      <p class="event-detail event-detail--rsvp">RSVP: DORA@DORAMILBY.EXAMPLE</p>
      <p class="event-detail event-detail--dress">DRESS CODE: <span class="dress-script">Lumeradazzle</span></p>
    </div>
  </article>

  <article class="invite invite--media">
    <div class="invite__haze"></div>
    <div class="invite__photo" role="img" aria-label="Photo of five cabaret dancers in pink feathered costumes with large pink feather fans"></div>
    <div class="invite__streak"></div>
    <div class="invite__marquee">WING IT!</div>
    <div class="invite__copy">
      <p class="kicker">VELVET HERON HAS ARRIVED IN BRISBANE</p>
      <h1 class="headline headline--grand">GRAND</h1>
      <h1 class="headline headline--opening">OPENING</h1>
      <p class="of-the">OF THE</p>
      <p class="venue-name venue-name--first">Velvet Heron</p>
      <p class="venue-name venue-name--second">Mirvolant</p>
      <div class="divider"></div>
      <p class="event-date">THURSDAY 7<sup>TH</sup> DECEMBER</p>
      <p class="event-title">MEDIA AND PUBLICITY PERFORMANCE OF LUMÈRA</p>
      <p class="event-detail event-detail--times">GATES OPEN 5:30 &nbsp;|&nbsp; SHOW START 7:30</p>
      <p class="event-detail event-detail--address">41 TARROWIN STREET, HAMILTON, QLD 4007</p>
      <p class="event-detail event-detail--rsvp">RSVP: HELLO@QUILLMARSH.EXAMPLE.AU</p>
      <p class="event-detail event-detail--dress">DRESS CODE: <span class="dress-script">Lumeradazzle</span></p>
    </div>
  </article>

  <article class="invite invite--listener">
    <div class="invite__haze"></div>
    <div class="invite__photo" role="img" aria-label="Photo of five cabaret dancers in pink feathered costumes with large pink feather fans"></div>
    <div class="invite__streak"></div>
    <div class="invite__marquee">WING IT!</div>
    <div class="invite__copy">
      <p class="kicker">VELVET HERON HAS ARRIVED IN BRISBANE</p>
      <h1 class="headline headline--grand">GRAND</h1>
      <h1 class="headline headline--opening">OPENING</h1>
      <p class="of-the">OF THE</p>
      <p class="venue-name venue-name--first">Velvet Heron</p>
      <p class="venue-name venue-name--second">Mirvolant</p>
      <div class="divider"></div>
      <p class="event-date">FRIDAY 8<sup>TH</sup> DECEMBER</p>
      <p class="event-title">ZUMO LISTENER PARTY FOR LUMÈRA</p>
      <p class="event-detail event-detail--times">GATES OPEN 5:30 &nbsp;|&nbsp; SHOW START 7:30</p>
      <p class="event-detail event-detail--address">41 TARROWIN STREET, HAMILTON, QLD 4007</p>
      <p class="event-detail event-detail--dress">DRESS CODE: <span class="dress-script">Lumeradazzle</span></p>
    </div>
  </article>

  <article class="invite invite--gala">
    <div class="invite__haze"></div>
    <div class="invite__photo" role="img" aria-label="Photo of five cabaret dancers in pink feathered costumes with large pink feather fans"></div>
    <div class="invite__streak"></div>
    <div class="invite__marquee">WING IT!</div>
    <div class="invite__copy">
      <p class="kicker">VELVET HERON HAS ARRIVED IN BRISBANE</p>
      <h1 class="headline headline--grand">GRAND</h1>
      <h1 class="headline headline--opening">OPENING</h1>
      <p class="of-the">OF THE</p>
      <p class="venue-name venue-name--first">Velvet Heron</p>
      <p class="venue-name venue-name--second">Mirvolant</p>
      <div class="divider"></div>
      <p class="event-date">SATURDAY 9<sup>TH</sup> DECEMBER</p>
      <p class="event-title">VELVET HERON GALA VIP OPENING LUMÈRA</p>
      <p class="event-detail event-detail--times">GATES OPEN 5:30 &nbsp;|&nbsp; SHOW START 7:30</p>
      <p class="event-detail event-detail--address">41 TARROWIN STREET, HAMILTON, QLD 4007</p>
      <p class="event-detail event-detail--rsvp">RSVP: MAREN@VHVX.EXAMPLE.AU</p>
      <p class="event-detail event-detail--dress">DRESS CODE: <span class="dress-script">Lumeradazzle</span></p>
      <p class="dress-note">(black tie)</p>
    </div>
  </article>

</body>
</html>
```